Create Website for new Home services company

We need a website built for a new home services company we are primarily a surface refinishing company that repairs cracks in tubs and resurfaces tubs, sinks or vanities also repainting cabinets as well.

```html
<!DOCTYPE html>
<html lang="en">
<head>
<meta charset="utf-8">
<title>Harwell Home Services</title>
<link href="https://fonts.googleapis.com/css2?family=Krona+One&family=Roboto:wght@400;500;700&family=Poppins:wght@400;600&display=swap" rel="stylesheet">
<style>
:root{
  --blue:#0e9fd1;
  --blue-dark:#0a86b4;
  --orange:#ff6a00;
  --ink:#1a1a1a;
  --text:#555;
  --pale:#e3f4fa;
  --footer:#000;
  --white:#fff;
}
*{margin:0;padding:0;box-sizing:border-box}
html,body{width:1200px;height:2973px;overflow:hidden;background:var(--white)}
body{position:relative;font-family:"Roboto",sans-serif;color:var(--ink)}
.abs{position:absolute}
.display{font-family:"Krona One",sans-serif;text-transform:uppercase}

/* header */
.topbar{left:332px;top:0;width:868px;height:60px;background:linear-gradient(90deg,var(--blue-dark),var(--blue));clip-path:polygon(0 0,100% 0,100% 100%,60px 100%)}
.contact{top:10px;display:flex;align-items:center;gap:16px;color:var(--white);font-size:16px;font-weight:500}
.contact .dot{width:44px;height:44px;border-radius:50%;background:var(--white);display:flex;align-items:center;justify-content:center}
.social-top{top:8px;left:928px;display:flex;gap:13px}
.social-top span{width:44px;height:44px;border:1.5px solid var(--white);border-radius:50%;display:flex;align-items:center;justify-content:center}
.social-top span i{width:10px;height:10px;border-radius:50%;background:var(--orange)}
.logo{left:112px;top:38px;display:flex;align-items:center;gap:10px}
.logo .mark{width:40px;height:40px;background:var(--blue)}
.logo .name{font-family:"Krona One",sans-serif;font-size:18px;color:var(--blue);line-height:1.25}
.nav{top:96px;font-size:16px;font-weight:500;color:var(--ink)}

/* hero */
.hero{left:0;top:152px;width:1200px;height:626px;background:linear-gradient(90deg,#f1f1f1 0%,#eaeaea 40%,#c9cdd2 60%,#6f86b8 80%,#3a56a8 100%)}
.hero-title{left:112px;font-size:60px;line-height:1}
.btn-outline{left:112px;top:588px;width:160px;height:52px;border:2px solid var(--orange);border-radius:3px;color:var(--orange);font-family:"Krona One",sans-serif;font-size:14px;display:flex;align-items:center;justify-content:center}

/* services */
.section-title{width:1200px;left:0;text-align:center;font-size:32px}
.card{top:955px;width:225px;height:315px}
.card .photo{position:absolute;inset:0;clip-path:polygon(0 40px,50% 0,100% 40px,100% 100%,0 100%)}
.card svg{position:absolute;left:0;top:0}
.card .label{position:absolute;left:0;right:0;top:254px;text-align:center;color:var(--white);font-family:"Krona One",sans-serif;font-size:14px}

/* about */
.about{left:0;top:1356px;width:1200px;height:573px;background:var(--pale)}
.frame{border:6px solid var(--white);box-shadow:0 4px 14px rgba(0,0,0,.18)}
.about-text{left:659px;top:1533px;width:430px;font-size:15.5px;line-height:25.7px;color:var(--text);text-align:justify}
.btn-solid{left:659px;top:1775px;width:159px;height:53px;background:var(--orange);border-radius:3px;color:var(--white);font-family:"Krona One",sans-serif;font-size:14px;display:flex;align-items:center;justify-content:center}

/* testimonials */
.map{left:213px;top:2112px;width:727px;height:381px;background:radial-gradient(ellipse at center,#eef0f3 0%,#f7f8f9 60%,transparent 75%)}
.avatar{border-radius:50%;background:linear-gradient(160deg,#c9b4a3,#7d6a5e)}
.quote{left:260px;top:2330px;width:680px;text-align:center;font-family:"Poppins",sans-serif;font-size:15.5px;line-height:25.7px;color:#333}
.author{left:0;width:1200px;top:2446px;text-align:center;font-family:"Poppins",sans-serif;font-weight:600;font-size:17px}

/* footer */
.footer{left:0;top:2615px;width:1200px;height:358px;background:var(--footer);color:var(--white)}
.foot-h{top:2709px;font-family:"Krona One",sans-serif;font-size:19px;color:var(--white)}
.email-box{left:110px;top:2767px;width:284px;height:51px;border:1.5px solid var(--white);border-radius:26px}
.email-box span{position:absolute;left:20px;top:16px;font-size:15px;color:#bbb}
.email-box b{position:absolute;right:5px;top:5px;width:84px;height:38px;border-radius:19px;background:var(--orange);font-size:15px;font-weight:700;display:flex;align-items:center;justify-content:center}
.links{left:452px;top:2763px;font-size:15.5px;line-height:25.7px;color:var(--white)}
.company{left:661px;top:2764px;font-size:15.5px;line-height:37px;color:var(--white)}
.company div{display:flex;align-items:center;gap:12px}
.social-foot{left:912px;top:2768px;display:flex;gap:18px}
.social-foot i{width:20px;height:20px;border-radius:50%;background:var(--white)}
.copy{left:0;width:1200px;top:2922px;text-align:center;font-size:15.5px;color:var(--white)}
</style>
</head>
<body>

<!-- header -->
<div class="abs topbar"></div>
<div class="abs contact" style="left:413px">
  <span class="dot"><svg width="18" height="18" viewBox="0 0 24 24"><path fill="#ff6a00" d="M6.6 10.8a15 15 0 006.6 6.6l2.2-2.2a1 1 0 011-.25 11.4 11.4 0 003.6.57 1 1 0 011 1V20a1 1 0 01-1 1A17 17 0 013 4a1 1 0 011-1h3.5a1 1 0 011 1c0 1.25.2 2.45.57 3.57a1 1 0 01-.25 1z"/></svg></span>
  +1 (555) 014 2290
</div>
<div class="abs contact" style="left:658px">
  <span class="dot"><svg width="18" height="14" viewBox="0 0 24 18"><rect width="24" height="18" rx="2" fill="#ff6a00"/><path d="M1 2l11 8 11-8" stroke="#fff" stroke-width="2" fill="none"/></svg></span>
  harwellhomeservices
</div>
<div class="abs social-top"><span><i></i></span><span><i></i></span><span><i></i></span></div>

<div class="abs logo"><span class="mark"></span><span class="name">HARWELL<br>HOME SERVICE</span></div>
<div class="abs nav" style="left:399px">HOME</div>
<div class="abs nav" style="left:508px">ABOUT US</div>
<div class="abs nav" style="left:647px">SERVICES</div>
<div class="abs nav" style="left:784px">TESTIMONIALS</div>
<div class="abs nav" style="left:962px">CONTACT US</div>

<!-- hero -->
<div class="abs hero" role="img" aria-label="Plumber in blue overalls repairing a bathroom sink with an orange tool bag"></div>
<h1 class="abs display hero-title" style="top:286px;color:var(--blue)">Harwell</h1>
<div class="abs display hero-title" style="top:380px;color:var(--orange)">Home</div>
<div class="abs display hero-title" style="top:475px;color:var(--blue)">Services</div>
<a class="abs btn-outline">GET STARTED</a>

<!-- services -->
<h2 class="abs display section-title" style="top:862px">Our <span style="color:var(--blue)">Services</span></h2>

<div class="abs card" style="left:15px">
  <div class="photo" role="img" aria-label="Hands fitting copper pipes and valves" style="background:linear-gradient(180deg,#c98a5a,#7a4a34 60%,#1c1c1c)"></div>
  <svg width="225" height="45"><polyline points="0,42 112.5,3 225,42" fill="none" stroke="#0e9fd1" stroke-width="7"/></svg>
  <div class="label">CRACKS IN TUBS</div>
</div>
<div class="abs card" style="left:252px">
  <div class="photo" role="img" aria-label="White tiled bathroom with a freestanding tub" style="background:linear-gradient(180deg,#e8e4df,#b3a79a 60%,#1c1c1c)"></div>
  <svg width="225" height="45"><polyline points="0,42 112.5,3 225,42" fill="none" stroke="#0e9fd1" stroke-width="7"/></svg>
  <div class="label">RESURFACES TUBS</div>
</div>
<div class="abs card" style="left:488px">
  <div class="photo" role="img" aria-label="Technician repairing pipes under a sink" style="background:linear-gradient(180deg,#d6d3cf,#6b6461 60%,#1c1c1c)"></div>
  <svg width="225" height="45"><polyline points="0,42 112.5,3 225,42" fill="none" stroke="#ff6a00" stroke-width="7"/></svg>
  <div class="label">SINKS</div>
</div>
<div class="abs card" style="left:725px">
  <div class="photo" role="img" aria-label="Modern vanity basin in a grey room with a plant" style="background:linear-gradient(180deg,#e2e4e3,#8f9694 60%,#1c1c1c)"></div>
  <svg width="225" height="45"><polyline points="0,42 112.5,3 225,42" fill="none" stroke="#0e9fd1" stroke-width="7"/></svg>
  <div class="label">VANITIES</div>
</div>
<div class="abs card" style="left:961px">
  <div class="photo" role="img" aria-label="Kitchen with wooden slatted cabinets" style="background:linear-gradient(180deg,#eee6dc,#a07a52 60%,#1c1c1c)"></div>
  <svg width="225" height="45"><polyline points="0,42 112.5,3 225,42" fill="none" stroke="#0e9fd1" stroke-width="7"/></svg>
  <div class="label">REPAINTING CABINETS</div>
</div>

<!-- about -->
<div class="abs about"></div>
<svg class="abs" style="left:130px;top:1565px" width="380" height="280">
  <polyline points="340,0 345,0 345,290" fill="none" stroke="#ff6a00" stroke-width="2"/>
  <polyline points="345,44 378,44 378,80" fill="none" stroke="#0e9fd1" stroke-width="2"/>
  <polyline points="0,230 0,236 90,236" fill="none" stroke="#ff6a00" stroke-width="2"/>
  <polyline points="37,230 37,278 90,278" fill="none" stroke="#0e9fd1" stroke-width="2"/>
</svg>
<div class="abs frame" role="img" aria-label="Plumber fixing the drain under a bathroom sink" style="left:121px;top:1431px;width:346px;height:360px;background:linear-gradient(135deg,#8a6b5a,#cfcfcf 55%,#6d6d6d)"></div>
<div class="abs frame" role="img" aria-label="Bright white kitchen with an island and wooden stools" style="left:220px;top:1641px;width:347px;height:215px;background:linear-gradient(180deg,#f2f0ec,#ddd6cc 60%,#a47b55)"></div>
<h2 class="abs display" style="left:659px;top:1455px;font-size:32px">About <span style="color:var(--blue)">Us</span></h2>
<p class="abs about-text">Lorem ipsum dolor sit amet, consectetur adipiscing elit, sed do eiusmod tempor incididunt ut labore et dolore magna aliqua. Ut enim ad minim veniam, quis nostrud exercitation ullamco laboris nisi ut aliquip ex ea commodo consequat. Duis aute irure dolor in reprehenderit in voluptate velit esse cillum dolore eu fugiat nulla pariatur. Excepteur sint occaecat cupidatat non proident, sunt in culpa qui officia deserunt mollit anim id est laborum.</p>
<a class="abs btn-solid">LEARN MORE</a>

<!-- testimonials -->
<h2 class="abs display section-title" style="top:2019px">What do people <span style="color:var(--blue)">say about us</span></h2>
<div class="abs map" role="img" aria-label="Dotted world map"></div>
<div class="abs avatar" role="img" aria-label="Customer portrait" style="left:274px;top:2174px;width:76px;height:76px"></div>
<div class="abs avatar" role="img" aria-label="Customer portrait" style="left:979px;top:2144px;width:76px;height:76px"></div>
<div class="abs avatar" role="img" aria-label="Customer portrait" style="left:847px;top:2226px;width:56px;height:56px"></div>
<div class="abs avatar" role="img" aria-label="Customer portrait" style="left:134px;top:2318px;width:66px;height:66px"></div>
<div class="abs avatar" role="img" aria-label="Customer portrait" style="left:906px;top:2441px;width:76px;height:76px"></div>
<div class="abs avatar" role="img" aria-label="Featured customer portrait" style="left:548px;top:2183px;width:104px;height:104px;border:6px solid var(--blue)"></div>
<p class="abs quote">“Lorem ipsum dolor sit amet, consectetur adipiscing elit, sed do eiusmod tempor incididunt ut labore et dolore magna aliqua. Ut enim ad minim veniam, quis nostrud exercitation ullamco laboris nisi ut aliquip ex ea commodo consequat.”</p>
<div class="abs author">Jonh Doe</div>

<!-- footer -->
<div class="abs footer"></div>
<h3 class="abs foot-h" style="left:112px">NEWSLETTER SIGN UP</h3>
<h3 class="abs foot-h" style="left:452px">QUICK LINKS</h3>
<h3 class="abs foot-h" style="left:661px">COMPANY</h3>
<h3 class="abs foot-h" style="left:912px">SOCIAL MEDIA</h3>
<div class="abs email-box"><span>Your Email</span><b>SUBMIT</b></div>
<nav class="abs links"><div>Home</div><div>About us</div><div>Services</div><div>Testimonials</div><div>Contact Us</div></nav>
<div class="abs company">
  <div><svg width="14" height="18" viewBox="0 0 14 20"><path fill="#fff" d="M7 0a7 7 0 00-7 7c0 5 7 13 7 13s7-8 7-13a7 7 0 00-7-7zm0 9.5A2.5 2.5 0 117 4.5a2.5 2.5 0 010 5z"/></svg>Lorem ipsum dolor sit</div>
  <div><svg width="16" height="16" viewBox="0 0 24 24"><path fill="#fff" d="M6.6 10.8a15 15 0 006.6 6.6l2.2-2.2a1 1 0 011-.25 11.4 11.4 0 003.6.57 1 1 0 011 1V20a1 1 0 01-1 1A17 17 0 013 4a1 1 0 011-1h3.5a1 1 0 011 1c0 1.25.2 2.45.57 3.57a1 1 0 01-.25 1z"/></svg>+1 (555) 014 2290</div>
  <div><svg width="17" height="13" viewBox="0 0 24 18"><rect width="24" height="18" rx="2" fill="#fff"/><path d="M1 2l11 8 11-8" stroke="#000" stroke-width="2" fill="none"/></svg>info@harwellhomeservices.com</div>
</div>
<div class="abs social-foot"><i></i><i></i><i></i><i></i><i></i></div>
<div class="abs copy">©Copyrights 2023 Harwell Home Services &nbsp;| &nbsp; All Rights Reserved</div>

</body>
</html>
```